I am looking for business cards and letterhead

I want a high-level look for CEO's who want a concierge level leadership consultant and organization development strategist

This needs to go with my brand: simple, elegant, clean. Please improve on this design while using these fonts and colors

Here is my website: CorinneHalvers.com

```html
<!DOCTYPE html>
<html lang="en">
<head>
<meta charset="utf-8">
<title>Corinne Halvers – Stationery Set 5</title>
<link href="https://fonts.googleapis.com/css2?family=Arimo:wght@400;700&family=PT+Sans:wght@400&display=swap" rel="stylesheet">
<style>
  :root{
    --navy:#0c1a40;
    --navy-deep:#070a1c;
    --teal:#4b9ba6;
    --teal-soft:#6fb5bd;
    --gold:#c9a45c;
    --paper:#ffffff;
    --stage-top:#d9c3a2;
    --stage-bottom:#2b2f31;
    --ink:#3a3f4a;
    --label:#ffffff;
    --ghost-leaf:#e3e9ee;
    --ghost-trunk:#f1ece3;
  }
  *{box-sizing:border-box;margin:0;padding:0}
  html,body{width:945px;height:1200px;overflow:hidden}
  body{position:relative;font-family:"Arimo",Arial,sans-serif;background:var(--stage-bottom)}
  .stage-top{position:absolute;left:0;top:0;width:945px;height:532px;background:var(--stage-top)}
  .stage-bottom{position:absolute;left:0;top:532px;width:945px;height:668px;background:var(--stage-bottom)}
  .set-label{position:absolute;font-family:"PT Sans",sans-serif;font-size:17px;color:var(--label);letter-spacing:.2px}

  /* wordmark standing in for the logo */
  .wordmark{display:flex;flex-direction:column;align-items:center;gap:5px;font-family:"Arimo",Arial,sans-serif;font-weight:700;color:var(--gold);text-transform:uppercase;letter-spacing:1.5px;white-space:nowrap}
  .wordmark .dot{border:2px solid var(--gold);border-radius:50%}

  /* business cards */
  .card{position:absolute;width:400px;height:228px;border-radius:22px;overflow:hidden;box-shadow:0 10px 22px rgba(0,0,0,.35)}
  .card-front{left:60px;top:95px;background:linear-gradient(135deg,#080c22 0%,var(--navy) 55%,#0a1638 100%)}
  .card-front .wordmark{position:absolute;left:0;right:0;top:52px;font-size:14px}
  .card-front .wordmark .dot{width:34px;height:34px}
  .card-front .rule{position:absolute;left:70px;right:70px;top:150px;height:1px;background:linear-gradient(90deg,transparent,var(--teal),transparent)}
  .card-front .tagline{position:absolute;left:0;right:0;top:162px;text-align:center;font-size:9.5px;color:var(--gold);letter-spacing:.6px}

  .card-back{left:485px;top:280px;background:var(--navy)}
  .card-back .photo{position:absolute;left:20px;top:40px;width:94px;height:84px;border:2px solid var(--teal);background:linear-gradient(180deg,#b9b4ad 0%,#7d7a78 55%,#1f2a44 100%)}
  .card-back .wordmark{position:absolute;right:22px;top:20px;font-size:9px;letter-spacing:1px}
  .card-back .wordmark .dot{width:26px;height:26px}
  .card-back .rule{position:absolute;left:120px;right:20px;top:128px;height:1px;background:var(--teal)}
  .card-back .name{position:absolute;left:20px;top:134px;font-size:12px;font-weight:700;color:var(--gold);letter-spacing:.5px}
  .card-back .cred{position:absolute;left:20px;top:149px;font-size:9px;color:var(--teal-soft)}
  .card-back .contacts{position:absolute;left:20px;top:166px}
  .card-back .address{position:absolute;right:0;bottom:14px;width:112px;height:46px;background:var(--teal);border-top-left-radius:14px;color:var(--navy-deep);font-size:8.5px;line-height:1.3;padding:10px 0 0 18px}
  .card-back .base{position:absolute;left:0;right:112px;bottom:0;height:14px;background:var(--navy-deep)}

  .contacts{list-style:none}
  .contacts li{display:flex;align-items:center;gap:6px;font-size:8.5px;color:#fff;line-height:13px}
  .contacts svg{width:9px;height:9px;flex:none}

  /* letterhead */
  .letterhead{position:absolute;left:77px;top:613px;width:375px;height:485px;background:var(--paper);overflow:hidden}
  .letterhead .wordmark{position:absolute;left:0;right:0;top:14px;font-size:10px}
  .letterhead .wordmark .dot{width:30px;height:30px}
  .letterhead .ghost-tree{position:absolute;left:8px;top:98px;width:358px;height:380px;border-radius:50% 50% 8px 8px / 60% 60% 8px 8px;background:radial-gradient(ellipse at 50% 35%,var(--ghost-leaf) 0%,#f2f5f8 45%,var(--ghost-trunk) 70%,rgba(255,255,255,0) 100%)}
  .letterhead .contacts{position:absolute;left:13px;top:434px}
  .letterhead .contacts li{color:var(--ink);font-size:7px;line-height:11px}
  .letterhead .address{position:absolute;right:0;bottom:0;width:92px;height:40px;background:var(--teal);clip-path:polygon(8px 0,100% 0,100% 100%,0 100%);text-align:center;font-size:7px;line-height:1.3;color:var(--navy-deep);padding-top:8px}
  .letterhead .base{position:absolute;left:0;right:92px;bottom:0;height:12px;background:var(--navy-deep)}

  /* envelope front */
  .env-front{position:absolute;left:503px;top:614px;width:385px;height:167px;background:var(--paper);overflow:hidden}
  .env-front .ghost-tree{position:absolute;right:0;top:14px;width:130px;height:140px;border-radius:50% 50% 6px 6px / 60% 60% 6px 6px;background:radial-gradient(ellipse at 50% 35%,var(--ghost-leaf) 0%,#f2f5f8 50%,var(--ghost-trunk) 75%,rgba(255,255,255,0) 100%)}
  .env-front .wordmark{position:absolute;left:12px;top:72px;font-size:8px;letter-spacing:1px}
  .env-front .wordmark .dot{width:26px;height:26px}
  .env-front .address{position:absolute;left:0;bottom:0;width:82px;height:29px;background:var(--teal);clip-path:polygon(0 0,70px 0,100% 100%,0 100%);border-top-right-radius:10px;font-size:6.5px;line-height:1.3;color:var(--navy-deep);padding:5px 0 0 13px}
  .env-front .base{position:absolute;left:82px;right:0;bottom:0;height:11px;background:var(--navy-deep)}

  /* envelope back */
  .env-back{position:absolute;left:503px;top:930px;width:385px;height:167px;background:var(--paper);overflow:hidden}
  .env-back svg.flap{position:absolute;left:0;top:0}
  .env-back .wordmark{position:absolute;left:0;right:0;top:27px;font-size:6.5px;letter-spacing:.8px}
  .env-back .wordmark .dot{width:18px;height:18px}
</style>
</head>
<body>
  <div class="stage-top"></div>
  <div class="stage-bottom"></div>

  <div class="set-label" style="left:77px;top:58px">Business card_5</div>

  <section class="card card-front">
    <div class="wordmark"><span class="dot"></span>Corinne Halvers</div>
    <div class="rule"></div>
    <p class="tagline">Elite Leadership Transformation and Organization Development</p>
  </section>

  <section class="card card-back">
    <div class="photo" role="img" aria-label="Portrait photograph of the consultant"></div>
    <div class="wordmark"><span class="dot"></span>Corinne Halvers</div>
    <div class="rule"></div>
    <h2 class="name">CORINNE HALVERS</h2>
    <p class="cred">MA / ABS</p>
    <ul class="contacts">
      <li><svg viewBox="0 0 10 10"><rect x="2.5" y=".5" width="5" height="9" rx="1" fill="none" stroke="#fff"/></svg>555-014-2290</li>
      <li><svg viewBox="0 0 10 10"><rect x=".5" y="2" width="9" height="6" fill="none" stroke="#fff"/><path d="M.5 2 5 6 9.5 2" fill="none" stroke="#fff"/></svg>info@corinnehalvers.com</li>
      <li><svg viewBox="0 0 10 10"><circle cx="5" cy="5" r="4.5" fill="none" stroke="#fff"/><path d="M.5 5h9M5 .5c-2.5 3-2.5 6 0 9M5 .5c2.5 3 2.5 6 0 9" fill="none" stroke="#fff" stroke-width=".8"/></svg>www.corinnehalvers.com</li>
    </ul>
    <div class="address">00 dummy city<br>dummy place 0000</div>
    <div class="base"></div>
  </section>

  <div class="set-label" style="left:77px;top:578px">Letterhead_5</div>
  <div class="set-label" style="left:503px;top:578px">ENV Front_5</div>
  <div class="set-label" style="left:503px;top:893px">ENV Back_5</div>

  <section class="letterhead">
    <div class="ghost-tree" role="img" aria-label="Faint large tree watermark"></div>
    <div class="wordmark"><span class="dot"></span>Corinne Halvers</div>
    <ul class="contacts">
      <li><svg viewBox="0 0 10 10"><rect x="2.5" y=".5" width="5" height="9" rx="1" fill="none" stroke="#c9a45c"/></svg>555-014-2290</li>
      <li><svg viewBox="0 0 10 10"><rect x=".5" y="2" width="9" height="6" fill="none" stroke="#c9a45c"/><path d="M.5 2 5 6 9.5 2" fill="none" stroke="#c9a45c"/></svg>info@corinnehalvers.com</li>
      <li><svg viewBox="0 0 10 10"><circle cx="5" cy="5" r="4.5" fill="none" stroke="#c9a45c"/><path d="M.5 5h9M5 .5c-2.5 3-2.5 6 0 9M5 .5c2.5 3 2.5 6 0 9" fill="none" stroke="#c9a45c" stroke-width=".8"/></svg>www.corinnehalvers.com</li>
    </ul>
    <div class="address">00 dummy city<br>dummy place 0000</div>
    <div class="base"></div>
  </section>

  <section class="env-front">
    <div class="ghost-tree" role="img" aria-label="Faint tree watermark"></div>
    <div class="wordmark"><span class="dot"></span>Corinne Halvers</div>
    <div class="address">00 dummy city<br>dummy place 0000</div>
    <div class="base"></div>
  </section>

  <section class="env-back">
    <svg class="flap" width="385" height="167" viewBox="0 0 385 167">
      <path d="M0 0H385C378 18 370 32 350 36L200 60C192 62 188 62 180 60L30 36C15 32 8 18 0 0Z" fill="var(--navy)"/>
    </svg>
    <div class="wordmark"><span class="dot"></span>Corinne Halvers</div>
  </section>
</body>
</html>
```